"Harbor Constructors" is a residential building company and needs a new business card design and may re

We would like a redesign based on the existing logo, and would like to see a new font as well. We are bespoke home builders who build sustainable energy efficient homes.

Industry/Entity Type

Construction

Contact Information for Business Card

Business card size 40mm x 90mm

Colors

Designer to choose colors to be used in the design.

```html
<!DOCTYPE html>
<html lang="en">
<head>
<meta charset="utf-8">
<title>Harbor Constructors – Business Card</title>
<link href="https://fonts.googleapis.com/css2?family=Montserrat:wght@400;500;700&display=swap" rel="stylesheet">
<style>
  :root {
    --backdrop: #3b3b3b;
    --card-white: #ffffff;
    --card-black: #1f1f1e;
    --ink: #3f3f3f;
    --ink-soft: #555555;
    --accent: #a8c83a;
    --mark-light: #dcdcdc;
  }
  * { margin: 0; padding: 0; box-sizing: border-box; }
  html, body {
    width: 1058px; height: 1200px; overflow: hidden;
    background: var(--backdrop);
    font-family: "Montserrat", sans-serif;
  }
  .canvas { position: relative; width: 1058px; height: 1200px; }
  .card {
    position: absolute; left: 79px; width: 900px; height: 400px;
    box-shadow: 0 10px 24px rgba(0,0,0,0.35);
  }
  .card--front { top: 130px; background: var(--card-white); color: var(--ink); }
  .card--back { top: 670px; background: var(--card-black); }

  .brand { position: absolute; display: flex; align-items: center; gap: 18px; }
  .brand__square { width: 62px; height: 62px; flex: none; }
  .brand__name { font-weight: 400; letter-spacing: 0.5px; line-height: 1; }
  .card--front .brand { top: 56px; right: 70px; }
  .card--front .brand__square { background: var(--ink); }
  .card--front .brand__name { font-size: 38px; color: var(--ink); }
  .card--back .brand { top: 50%; left: 50%; transform: translate(-50%, -50%); gap: 26px; }
  .card--back .brand__square { width: 96px; height: 96px; background: var(--accent); }
  .card--back .brand__name { font-size: 54px; color: var(--mark-light); }

  .person { position: absolute; top: 120px; left: 48px; }
  .person__name { font-size: 34px; font-weight: 400; color: var(--ink-soft); }
  .person__name strong { font-weight: 700; color: var(--ink); }
  .person__phone { font-size: 30px; font-weight: 500; margin-top: 4px; }

  .contact { position: absolute; left: 48px; bottom: 88px; list-style: none; }
  .contact__item { display: flex; align-items: center; gap: 14px; font-size: 22px; font-weight: 500; line-height: 1.55; }
  .contact__icon { width: 22px; height: 22px; flex: none; }
  .registration { position: absolute; left: 48px; bottom: 38px; font-size: 22px; font-weight: 500; color: var(--accent); }
</style>
</head>
<body>
<main class="canvas">
  <section class="card card--front" aria-label="Business card front">
    <div class="brand">
      <span class="brand__square"></span>
      <span class="brand__name">harbor constructors</span>
    </div>
    <div class="person">
      <p class="person__name">Daniel <strong>Marlowe</strong></p>
      <p class="person__phone">0400 555 018</p>
    </div>
    <ul class="contact">
      <li class="contact__item">
        <svg class="contact__icon" viewBox="0 0 24 24" aria-hidden="true"><rect x="2" y="5" width="20" height="14" fill="#a8c83a"/><path d="M2 5l10 8 10-8" fill="none" stroke="#fff" stroke-width="1.6"/></svg>
        daniel@harborconstructors.com.au
      </li>
      <li class="contact__item">
        <svg class="contact__icon" viewBox="0 0 24 24" aria-hidden="true" fill="none" stroke="#a8c83a" stroke-width="1.6"><circle cx="12" cy="12" r="9.5"/><ellipse cx="12" cy="12" rx="4.5" ry="9.5"/><path d="M2.5 12h19M4 7h16M4 17h16"/></svg>
        www.harborconstructors.com.au
      </li>
      <li class="contact__item">
        <svg class="contact__icon" viewBox="0 0 24 24" aria-hidden="true"><path d="M12 1.5a7.5 7.5 0 0 0-7.5 7.5c0 5.5 7.5 13.5 7.5 13.5s7.5-8 7.5-13.5A7.5 7.5 0 0 0 12 1.5z" fill="#a8c83a"/><circle cx="12" cy="9" r="3" fill="#fff"/></svg>
        PO Box 2210 Eastgate LPO Kelmscott WA 6111
      </li>
    </ul>
    <p class="registration">Registration 40517 ABN: 12 345 678 901</p>
  </section>

  <section class="card card--back" aria-label="Business card back">
    <div class="brand">
      <span class="brand__square"></span>
      <span class="brand__name">harbor constructors</span>
    </div>
  </section>
</main>
</body>
</html>
```